Business Card - Rebranding for Consulting Firm

We are renaming and rebranding our consulting firm and need to raise the level of quality of our cards as part of that effort. We consult to leading high tech, life science and other innovation sector companies.

Need a two-sided business card design.

Side 1: (a) Company logo (b) tag line: Optimize Your Investment in Talent (c) Name (d) Title (e) Phone 1: Office (f) Phone 2: Mobile (g) email: person@HollowmereAdvisory.com

Side 2: Two lines of text: (a) Growth is Imperative. Change is Constant. Talent Executes Strategy. (b) We help you excel at all three.

Target Market(s)

Business and human resources executives and senior managers

Industry/Entity Type

Management Consulting

Contact Information for Business Card

Font styles to use
Sans Serif

Requirements
Must have
• clean, not too busy, but with a bit of creativity. Stick to the colors used in the attached logo
• appeal to high tech, life science companies
Nice to have
• prefer white background

```html
<!DOCTYPE html>
<html lang="en">
<head>
<meta charset="utf-8">
<title>Hollowmere Advisory – Business Card</title>
<link rel="stylesheet" href="https://fonts.googleapis.com/css2?family=Lato:ital,wght@0,400;0,700;1,700&family=Exo+2:ital,wght@1,600&display=swap">
<style>
  :root {
    --backdrop: #e9ebee;
    --card: #ffffff;
    --brand-blue: #1466a8;
    --accent-blue: #1a9ad6;
    --slate: #7b8a9a;
    --slate-dark: #5f6f80;
  }
  * { box-sizing: border-box; margin: 0; padding: 0; }
  html, body {
    width: 1200px; height: 1200px; overflow: hidden;
    background: var(--backdrop);
    font-family: "Lato", sans-serif;
  }
  .canvas {
    width: 1200px; height: 1200px;
    display: flex; flex-direction: column;
    align-items: center; justify-content: center; gap: 44px;
  }
  .card {
    position: relative;
    width: 900px; height: 514px;
    background: var(--card);
    box-shadow: 0 6px 22px rgba(40, 55, 75, 0.16);
  }

  /* Back side */
  .card-back { display: flex; flex-direction: column; align-items: center; justify-content: center; }
  .back-mark { display: flex; align-items: center; gap: 22px; margin-bottom: 54px; }
  .back-mark .mark-square { width: 54px; height: 54px; background: var(--accent-blue); }
  .back-mark .mark-name {
    font-weight: 700; font-size: 76px; color: var(--brand-blue); letter-spacing: -1px;
  }
  .statement {
    text-align: center; color: var(--slate);
    font-size: 17px; letter-spacing: 0.6px; text-transform: uppercase; line-height: 1.55;
  }

  /* Front side */
  .brand { position: absolute; left: 56px; top: 50px; }
  .brand-row { display: flex; align-items: center; gap: 16px; }
  .brand-square { width: 34px; height: 34px; background: var(--accent-blue); }
  .brand-name { font-weight: 700; font-size: 62px; line-height: 1; color: var(--brand-blue); letter-spacing: -1px; }
  .brand-sub {
    margin: 6px 0 0 50px; font-size: 13px; letter-spacing: 9px; color: var(--slate);
  }
  .tagline {
    margin-top: 12px;
    font-family: "Exo 2", sans-serif; font-style: italic; font-weight: 600;
    font-size: 17px; letter-spacing: 4px; color: var(--brand-blue);
  }
  .person { position: absolute; left: 70px; top: 300px; }
  .person-name { font-weight: 700; font-style: italic; font-size: 30px; color: var(--brand-blue); }
  .person-title { font-size: 27px; color: var(--slate); margin-top: 2px; }
  .divider {
    position: absolute; left: 440px; top: 278px; width: 2px; height: 172px; background: var(--slate);
  }
  .contact { position: absolute; left: 480px; top: 290px; color: var(--slate); }
  .address { font-size: 24px; line-height: 1.15; margin-bottom: 24px; }
  .contact-list { list-style: none; font-size: 24px; line-height: 1.35; }
  .contact-list li { display: flex; align-items: center; gap: 12px; }
  .contact-list svg { width: 18px; height: 18px; flex: none; fill: var(--brand-blue); }
</style>
</head>
<body>
<main class="canvas">

  <section class="card card-back" aria-label="Card back">
    <div class="back-mark">
      <span class="mark-square"></span>
      <span class="mark-name">Hollowmere</span>
    </div>
    <p class="statement">
      Growth is imperative. Change is constant. Talent executes strategy.<br>
      We help you excel at all three.
    </p>
  </section>

  <section class="card card-front" aria-label="Card front">
    <div class="brand">
      <div class="brand-row">
        <span class="brand-square"></span>
        <span class="brand-name">Hollowmere</span>
      </div>
      <div class="brand-sub">ADVISORY LLC</div>
      <div class="tagline">Optimize Your Investment in Talent</div>
    </div>

    <div class="person">
      <div class="person-name">Elin Marsh</div>
      <div class="person-title">Marketing Director</div>
    </div>

    <div class="divider"></div>

    <div class="contact">
      <p class="address">Havnegata 27, 0150 Oslo<br>Norway</p>
      <ul class="contact-list">
        <li>
          <svg viewBox="0 0 20 20" aria-hidden="true"><path d="M2 7c0-2 4-4 8-4s8 2 8 4v2h-4V7H6v2H2z"/><rect x="4" y="10" width="12" height="7" rx="1"/></svg>
          Phone Office
        </li>
        <li>
          <svg viewBox="0 0 20 20" aria-hidden="true"><path d="M6 2h8a1 1 0 0 1 1 1v14a1 1 0 0 1-1 1H6a1 1 0 0 1-1-1V3a1 1 0 0 1 1-1zm1 2v6h6V4z"/></svg>
          Phone Mobile
        </li>
        <li>
          <svg viewBox="0 0 20 20" aria-hidden="true"><path d="M2 5h16v10H2z M2 5l8 6 8-6" stroke="#fff" stroke-width="1.2"/></svg>
          person@HollowmereAdvisory.com
        </li>
      </ul>
    </div>
  </section>

</main>
</body>
</html>
```